Information One Page for Email

I am looking for a informative attachment I can send with an introductive email for Maplecrest Slab Works. Something I can also Mail.

Maplecrest Slab Works is the leader in Rebar Post Tension Cable Placement and Post Tension Cable repair. Outside of cable placement and repair we do concrete repair, Parking Garage restoration and

Content

Post Tension Repair and Concrete Restoration
Post-tensioning is a revolutionary method in concrete construction that enhances the strength and durability of structures. However, like all construction ele-ments, post-tension cables can experience wear and damage over time. Ensuring timely and effective repair is crucial for maintaining the safety and integrity of your building.
Why Post-Tension Cable Repair is Essential
1. **Structural Integrity**: Damaged or deteriorated cables can compromise the structural integrity of your building, leading to safety hazards and potential structural failures.
2. **Extended Lifespan**: Regular maintenance and repair of post-tension cables extend the lifespan of your structure, ensuring it remains safe and function-al for years to come.
3. **Cost-Effective**: Addressing cable issues early on prevents more severe damage and costly repairs down the line.
Common Signs of Post-Tension Cable Issues
- Cracks in concrete surfaces
- Unusual noises or popping sounds
- Visible cable ends or broken strands
- Water leakage through cracks
Our Repair Process
1. **Inspection and Assessment**: Our team conducts a thorough inspection to identify the extent of the damage and determine the appropriate repair meth-ods.
2. **Cable Repair or Replacement**: Depending on the severity, we either re-pair the existing cables or replace them with new ones to restore full functional-ity.
3. **Sealing and Protection**: After repairing, we seal the affected areas to protect against moisture and future damage.
4. **Quality Assurance**: We perform rigorous quality checks to ensure the repairs meet industry standards and the structure is safe for use.
Why Choose Us
- **Expertise and Experience**: With years of experience in post-tension cable repair, our team is skilled in handling even the most complex repairs efficiently and effectively.
- **Advanced Technology**: We use the latest technology and materials to ensure durable and long-lasting repairs.
- **Customer Satisfaction**: Our commitment to quality and customer satisfaction sets us apart. We work closely with our clients to ensure their needs are met and expectations exceeded.
Contact Us
If you suspect issues with your post-tension cables or need a routine inspection, don't hesitate to contact us. Our experts are ready to provide the best solutions to keep your structures safe and secure.
Ensure the safety and longevity of your building with our professional post-tension cable repair services. Trust us to deliver quality and reliability every time.

```html
<!DOCTYPE html>
<html lang="en">
<head>
<meta charset="utf-8">
<title>Maplecrest Slab Works – Post Tension Repair and Concrete Restoration</title>
<link href="https://fonts.googleapis.com/css2?family=Anton&family=Manrope:wght@300;400;500;600;700;800&display=swap" rel="stylesheet">
<style>
  :root{
    --green:#17693d;
    --green-dark:#115230;
    --ink:#2f2f2f;
    --body:#555;
    --grey-band:#e6e7e9;
    --stage:#a7a7a7;
    --white:#fff;
    --sky:#cfe6f3;
  }
  *{box-sizing:border-box;margin:0;padding:0}
  html,body{width:1200px;height:2238px;overflow:hidden;background:var(--stage)}
  body{position:relative;font-family:"Manrope",sans-serif;color:var(--body)}
  .page{position:absolute;left:206px;width:788px;height:1020px;background:var(--white);overflow:hidden;box-shadow:4px 6px 10px rgba(0,0,0,.25)}
  .page--front{top:76px}
  .page--back{top:1135px}
  .abs{position:absolute}
  .page-art{position:absolute;left:0;top:0}

  /* front */
  .brand{left:62px;top:40px;display:flex;align-items:center;gap:10px;font-weight:700;font-size:24px;color:var(--green)}
  .brand-mark{width:16px;height:16px;background:var(--green)}
  .headline{left:62px;top:132px;font-family:"Anton",sans-serif;font-size:56px;line-height:61px;color:var(--green);letter-spacing:.2px}
  .intro{left:62px;top:738px;width:300px;font-size:14.3px;line-height:23.3px;color:var(--body)}
  .intro strong{color:var(--green);font-weight:700}
  .site{left:62px;top:953px;font-size:19px;font-weight:700;color:var(--green)}
  .essential-title{left:458px;top:594px;font-size:20.5px;line-height:26px;font-weight:700;color:var(--white)}
  .benefit{left:458px;width:300px;color:var(--white)}
  .benefit h3{font-size:14px;font-weight:700;margin-bottom:6px}
  .benefit p{font-size:13.4px;line-height:18.6px;font-weight:400}

  /* back */
  .signs{left:69px;top:40px}
  .signs h2{font-size:16.5px;line-height:21px;font-weight:700;color:var(--green)}
  .signs ul{list-style:none;margin-top:12px}
  .signs li{position:relative;padding-left:32px;font-size:14px;font-weight:600;color:var(--ink);height:28px}
  .signs li::before{content:"";position:absolute;left:3px;top:5px;border-left:9px solid var(--green);border-top:5px solid transparent;border-bottom:5px solid transparent}
  .process{left:43px;top:221px;width:699px;height:304px;background:var(--green);border-radius:14px;box-shadow:0 5px 0 rgba(0,0,0,.08)}
  .process-title{position:absolute;left:0;right:0;top:14px;text-align:center;font-size:21px;font-weight:700;color:var(--white)}
  .step{position:absolute;width:240px;color:var(--white)}
  .step h3{font-size:14px;font-weight:700;margin-bottom:6px}
  .step p{font-size:13.4px;line-height:18.6px}
  .step-icon{position:absolute;width:50px;height:50px}
  .choose-title{left:0;width:788px;top:551px;text-align:center;font-size:21px;font-weight:700;color:var(--green)}
  .reason{top:578px;width:200px;text-align:center}
  .reason h3{margin-top:8px;font-size:14px;font-weight:700;color:var(--green)}
  .reason p{margin-top:6px;font-size:13.4px;line-height:18.6px;color:var(--body)}
  .divider{top:600px;width:1px;height:160px;background:var(--green)}
  .call{left:0;width:788px;top:766px;text-align:center;font-size:67px;font-weight:800;letter-spacing:-1.5px;color:var(--green);line-height:80px}
  .visit{left:109px;top:862px;width:570px;height:35px;border-radius:18px;background:var(--green);color:var(--white);text-align:center;font-size:20.5px;font-weight:700;line-height:35px;box-shadow:0 3px 0 rgba(0,0,0,.15)}
  .cta{left:0;width:788px;top:902px;text-align:center;font-size:24px;font-weight:300;color:var(--ink)}
  .fineprint{left:62px;top:947px;width:674px;font-size:9.6px;line-height:14px;color:#666}
  .foot-band{left:0;bottom:0;width:788px;height:11px;background:var(--green)}
</style>
</head>
<body>

<section class="page page--front">
  <svg class="page-art" width="788" height="1020" viewBox="0 0 788 1020">
    <defs>
      <linearGradient id="sky" x1="0" y1="0" x2="1" y2="0">
        <stop offset="0" stop-color="#bfdff0"/><stop offset=".5" stop-color="#eef6fb"/><stop offset="1" stop-color="#ffffff"/>
      </linearGradient>
      <linearGradient id="facade" x1="0" y1="0" x2="1" y2="1">
        <stop offset="0" stop-color="#d9dcdc"/><stop offset=".5" stop-color="#b9b6ae"/><stop offset="1" stop-color="#8f8c86"/>
      </linearGradient>
      <linearGradient id="garage" x1="0" y1="0" x2="0" y2="1">
        <stop offset="0" stop-color="#c9d2d8"/><stop offset="1" stop-color="#8d8f8e"/>
      </linearGradient>
      <linearGradient id="cables" x1="0" y1="0" x2="0" y2="1">
        <stop offset="0" stop-color="#b5c4cc"/><stop offset=".4" stop-color="#6aa8c4"/><stop offset="1" stop-color="#9a6f60"/>
      </linearGradient>
      <linearGradient id="tower" x1="0" y1="0" x2="0" y2="1">
        <stop offset="0" stop-color="#d6d4cf"/><stop offset="1" stop-color="#9e948a"/>
      </linearGradient>
    </defs>
    <rect width="788" height="700" fill="url(#sky)"/>
    <path role="img" aria-label="Photo: balconies of a concrete tower under repair, seen from below against the sky" d="M300 0H788V420Q560 420 330 400L300 0Z" fill="url(#facade)"/>
    <path d="M0 700V620Q300 470 788 445V1020H0Z" fill="var(--white)"/>
    <path d="M0 628Q300 480 560 455" fill="none" stroke="var(--green)" stroke-width="14"/>
    <path d="M407 995V610Q407 594 423 594H560V437H788V995H407Z" fill="var(--green)"/>
    <path d="M423 995H407V979Q407 995 423 995Z" fill="var(--white)"/>
    <g>
      <circle cx="165" cy="567" r="135" fill="var(--green)"/>
      <circle cx="165" cy="567" r="124" fill="var(--white)"/>
      <circle role="img" aria-label="Photo: parking garage deck beside a high-rise building" cx="165" cy="567" r="115" fill="url(#garage)"/>
      <circle cx="382" cy="467" r="128" fill="var(--green)"/>
      <circle cx="382" cy="467" r="118" fill="var(--white)"/>
      <circle role="img" aria-label="Photo: blue post-tension cables laid out on a slab deck" cx="382" cy="467" r="109" fill="url(#cables)"/>
      <circle cx="624" cy="432" r="128" fill="var(--green)"/>
      <circle cx="624" cy="432" r="118" fill="var(--white)"/>
      <circle role="img" aria-label="Photo: high-rise facade with balcony slabs being restored" cx="624" cy="432" r="109" fill="url(#tower)"/>
    </g>
    <g fill="var(--green)" stroke="var(--white)" stroke-width="3.5">
      <circle cx="407" cy="687" r="28"/><circle cx="407" cy="809" r="28"/><circle cx="407" cy="926" r="28"/>
    </g>
    <g fill="none" stroke="var(--white)" stroke-width="1.8" stroke-linecap="round">
      <path d="M392 698h30M394 691h26M394 684h26M396 677h22M400 670h14M397 691v7M407 684v14M417 691v7"/>
      <rect x="400" y="802" width="14" height="14"/>
      <path d="M391 793l6 6M391 793h5M391 793v5M423 793l-6 6M423 793h-5M423 793v5M391 825l6-6M391 825h5M391 825v-5M423 825l-6-6M423 825h-5M423 825v-5"/>
      <path d="M393 930q8-6 16 0l6-4q4-1 4 3l-12 10h-14z"/>
      <circle cx="410" cy="918" r="7"/>
      <path d="M404 910l12 0"/>
    </g>
  </svg>

  <div class="abs brand"><span class="brand-mark"></span>Maplecrest Slab Works</div>
  <h1 class="abs headline">Post Tension<br>Repair and<br>Concrete<br>Restoration</h1>

  <p class="abs intro"><strong>Post-tensioning</strong> is a revolutionary method in concrete construction that enhances the strength and durability of structures. However, like all construction ele-ments, post-tension cables can experience wear and damage over time. Ensuring timely and effective repair is crucial for maintaining the safety and integrity of your building.</p>
  <p class="abs site">maplecrestslabworks.com</p>

  <h2 class="abs essential-title">WHY POST-TENSION CABLE<br>REPAIR IS ESSENTIAL</h2>
  <div class="abs benefit" style="top:659px">
    <h3>Structural Integrity</h3>
    <p>Damaged or deteriorated cables can compromise the structural integrity of your building, leading to safety hazards and potential structural failures.</p>
  </div>
  <div class="abs benefit" style="top:779px">
    <h3>Extended Lifespan</h3>
    <p>Regular maintenance and repair of post-tension cables extend the lifespan of your structure, ensuring it remains safe and function-al for years to come.</p>
  </div>
  <div class="abs benefit" style="top:896px">
    <h3>Cost-Effective</h3>
    <p>Addressing cable issues early on prevents more severe damage and costly repairs down the line.</p>
  </div>
</section>

<section class="page page--back">
  <svg class="page-art" width="788" height="1020" viewBox="0 0 788 1020">
    <defs>
      <linearGradient id="worker" x1="0" y1="0" x2="0" y2="1">
        <stop offset="0" stop-color="#dcdad4"/><stop offset=".55" stop-color="#6b6760"/><stop offset="1" stop-color="#b7b2a8"/>
      </linearGradient>
    </defs>
    <rect y="334" width="788" height="428" fill="var(--grey-band)"/>
    <circle cx="705" cy="30" r="342" fill="var(--green)"/>
    <circle role="img" aria-label="Photo: worker with a jackhammer breaking out a damaged concrete balcony slab" cx="705" cy="30" r="334" fill="url(#worker)"/>
  </svg>

  <div class="abs signs">
    <h2>Common Signs of Post-Tension<br>Cable Issues</h2>
    <ul>
      <li>Cracks in concrete surfaces</li>
      <li>Unusual noises or popping sounds</li>
      <li>Visible cable ends or broken strands</li>
      <li>Water leakage through cracks</li>
    </ul>
  </div>

  <div class="abs process">
    <h2 class="process-title">OUR REPAIR PROCESS</h2>

    <svg class="step-icon" style="left:26px;top:57px" viewBox="0 0 50 50"><circle cx="25" cy="25" r="24" fill="var(--white)"/><g fill="none" stroke="var(--green)" stroke-width="2.2" stroke-linecap="round"><circle cx="28" cy="22" r="11"/><circle cx="28" cy="22" r="6.5"/><path d="M25 22l2.5 2.5 4-4.5M20 30l-8 8"/></g></svg>
    <div class="step" style="left:99px;top:57px">
      <h3>Inspection and Assessment</h3>
      <p>Our team conducts a thorough inspection to identify the extent of the damage and determine the appropriate repair meth-ods.</p>
    </div>

    <svg class="step-icon" style="left:364px;top:57px" viewBox="0 0 50 50"><circle cx="25" cy="25" r="24" fill="var(--white)"/><g fill="none" stroke="var(--green)" stroke-width="2.2" stroke-linejoin="round" stroke-linecap="round"><path d="M25 9l13 5v9c0 9-6 15-13 18-7-3-13-9-13-18v-9z"/><path d="M19 25l4.5 4.5L32 21"/></g></svg>
    <div class="step" style="left:437px;top:56px">
      <h3>Sealing and Protection</h3>
      <p>After repairing, we seal the affected areas to protect against moisture and future damage.</p>
    </div>

    <svg class="step-icon" style="left:26px;top:183px" viewBox="0 0 50 50"><circle cx="25" cy="25" r="24" fill="var(--white)"/><g fill="none" stroke="var(--green)" stroke-width="2.2" stroke-linecap="round"><path d="M12 34q6-2 9-8t9-10M20 38q6-3 9-9t9-9"/><path d="M24 12v4M30 10l-1 4M18 15l2 3M34 34l-3-2M38 28l-4-1"/></g></svg>
    <div class="step" style="left:99px;top:181px">
      <h3>Cable Repair or Replacemen</h3>
      <p>Depending on the severity, we either re-pair the existing cables or replace them with new ones to restore full functional-ity.</p>
    </div>

    <svg class="step-icon" style="left:364px;top:183px" viewBox="0 0 50 50"><circle cx="25" cy="25" r="24" fill="var(--white)"/><g fill="none" stroke="var(--green)" stroke-width="2.2" stroke-linecap="round" stroke-linejoin="round"><path d="M25 8l4 3 5-1 1 5 4 3-2 5 2 5-4 3-1 5-5-1-4 3-4-3-5 1-1-5-4-3 2-5-2-5 4-3 1-5 5 1z"/><circle cx="25" cy="25" r="8.5"/><path d="M21 25l3 3 5-6"/></g></svg>
    <div class="step" style="left:437px;top:181px">
      <h3>Quality Assurance</h3>
      <p>We perform rigorous quality checks to ensure the repairs meet industry standards and the structure is safe for use.</p>
    </div>
  </div>

  <h2 class="abs choose-title">WHY CHOOSE US</h2>
  <div class="abs divider" style="left:263px"></div>
  <div class="abs divider" style="left:527px"></div>

  <div class="abs reason" style="left:54px">
    <svg width="20" height="20" viewBox="0 0 20 20"><circle cx="10" cy="10" r="10" fill="var(--green)"/><path d="M5.5 10.5l3 3 6-6.5" fill="none" stroke="var(--white)" stroke-width="2.2" stroke-linecap="round" stroke-linejoin="round"/></svg>
    <h3>Expertise and Experience</h3>
    <p>With years of experience in post-tension cable repair, our team is skilled in handling even the most complex repairs efficiently and effectively.</p>
  </div>
  <div class="abs reason" style="left:294px">
    <svg width="20" height="20" viewBox="0 0 20 20"><circle cx="10" cy="10" r="10" fill="var(--green)"/><path d="M5.5 10.5l3 3 6-6.5" fill="none" stroke="var(--white)" stroke-width="2.2" stroke-linecap="round" stroke-linejoin="round"/></svg>
    <h3>Customer Satisfaction</h3>
    <p>Our commitment to quality and customer satisfaction sets us apart. We work closely with our clients to ensure their needs are met and expectations exceeded.</p>
  </div>
  <div class="abs reason" style="left:539px">
    <svg width="20" height="20" viewBox="0 0 20 20"><circle cx="10" cy="10" r="10" fill="var(--green)"/><path d="M5.5 10.5l3 3 6-6.5" fill="none" stroke="var(--white)" stroke-width="2.2" stroke-linecap="round" stroke-linejoin="round"/></svg>
    <h3>Advanced Technology</h3>
    <p>We use the latest technology and materials to ensure durable and long-lasting repairs.</p>
  </div>

  <p class="abs call">CALL (555) 014-2387</p>
  <p class="abs visit">AND VISIT WWW.MAPLECRESTSLABWORKS.COM</p>
  <p class="abs cta">to start your construction project!</p>
  <p class="abs fineprint">If you suspect issues with your post-tension cables or need a routine inspection, don't hesitate to contact us. Our experts are ready to provide the best solutions to keep your structures safe and secure. Ensure the safety and longevity of your building with our professional post-tension cable repair services. Trust us to deliver quality and reliability every time.</p>
  <div class="abs foot-band"></div>
</section>

</body>
</html>
```